Bouncy Castle and Softplay Flyer

Flyer to attract schools and clients to book our bouncy castle and softplay company

Target Market(s)

Schools, Nurseries, private clients

Industry/Entity Type

Entertainment

Requirements
Nice to have
• Fun and quirky

```html
<!DOCTYPE html>
<html lang="en">
<head>
<meta charset="utf-8">
<title>Bouncewell Events – Bouncy Castle and Softplay Flyer</title>
<link rel="stylesheet" href="https://fonts.googleapis.com/css2?family=Lilita+One&family=Poppins:wght@600;700;800;900&display=swap">
<style>
  :root {
    --sun-top: #ffb21e;
    --sun-bottom: #ffcf3a;
    --berry: #ec4a6e;
    --berry-deep: #e23a62;
    --berry-light: #f56e8a;
    --leaf: #49c42f;
    --leaf-dark: #1f7a17;
    --white: #ffffff;
    --sparkle: #ffffff;
    --sparkle-blue: #2fb9e8;
  }
  * { margin: 0; padding: 0; box-sizing: border-box; }
  html, body { width: 849px; height: 1200px; overflow: hidden; }
  body { font-family: "Poppins", sans-serif; background: var(--berry); }
  .flyer {
    position: relative;
    width: 849px;
    height: 1200px;
    overflow: hidden;
    background: linear-gradient(180deg, var(--sun-top) 0%, var(--sun-bottom) 40%);
  }
  .backdrop { position: absolute; inset: 0; width: 849px; height: 1200px; }
  .brand {
    position: absolute;
    left: 0; right: 0;
    top: 118px;
    display: flex;
    align-items: center;
    justify-content: center;
    gap: 12px;
  }
  .brand-dot { width: 22px; height: 22px; border-radius: 50%; background: var(--berry-deep); }
  .brand-name {
    font-family: "Lilita One", "Poppins", sans-serif;
    font-weight: 400;
    font-size: 42px;
    line-height: 1;
    color: var(--berry-deep);
    text-transform: uppercase;
    letter-spacing: 1px;
  }
  .child {
    position: absolute;
    border-radius: 46% 46% 12px 12px;
  }
  .child--boy {
    left: 62px; top: 196px; width: 230px; height: 300px;
    background: linear-gradient(180deg, #f3d2b5 0%, #f4f1ee 55%, #e6e1dc 100%);
  }
  .child--girl {
    left: 556px; top: 190px; width: 236px; height: 310px;
    background: linear-gradient(180deg, #f0d08c 0%, #f3cdb3 40%, #f6a7b8 75%, #f7d36b 100%);
  }
  .snapshot {
    position: absolute;
    border: 9px solid var(--white);
    border-radius: 6px;
    box-shadow: 0 8px 18px rgba(0,0,0,0.22);
  }
  .snapshot--left {
    left: 62px; top: 610px; width: 280px; height: 270px;
    transform: rotate(-8deg);
    background: linear-gradient(180deg, #c9c6c2 0%, #d8333c 45%, #3a7a2a 100%);
  }
  .snapshot--right {
    left: 508px; top: 570px; width: 290px; height: 280px;
    transform: rotate(7deg);
    background: linear-gradient(180deg, #bcc9d6 0%, #4fae3a 50%, #2f7a25 100%);
  }
  .snapshot--centre {
    left: 252px; top: 420px; width: 348px; height: 300px;
    transform: rotate(-2deg);
    background: linear-gradient(180deg, #b9cbe0 0%, #d8313c 45%, #2b59b8 80%, #4a8f35 100%);
    z-index: 2;
  }
  .headline {
    position: absolute;
    left: 0; right: 0; top: 900px;
    text-align: center;
    font-family: "Lilita One", "Poppins", sans-serif;
    font-weight: 400;
    font-size: 84px;
    line-height: 1;
    color: var(--leaf);
    text-transform: uppercase;
    letter-spacing: 2px;
    -webkit-text-stroke: 3px var(--leaf-dark);
    paint-order: stroke fill;
    text-shadow:
      4px 4px 0 var(--white),
      -3px -3px 0 var(--white),
      3px -3px 0 var(--white),
      -3px 3px 0 var(--white);
  }
  .call-to-action {
    position: absolute;
    left: 0; right: 0; top: 1080px;
    text-align: center;
    color: var(--white);
    font-weight: 700;
    font-size: 30px;
    line-height: 1.3;
  }
</style>
</head>
<body>
<main class="flyer">
  <svg class="backdrop" viewBox="0 0 849 1200" aria-hidden="true">
    <path d="M0 470 C 160 410, 300 520, 460 470 S 760 380, 849 420 L 849 1200 L 0 1200 Z" fill="var(--berry-light)"/>
    <path d="M0 520 C 180 470, 320 560, 480 520 S 760 440, 849 470 L 849 1200 L 0 1200 Z" fill="var(--berry)"/>
    <path d="M-10 150 C 90 60, 170 40, 260 10" fill="none" stroke="var(--white)" stroke-width="5" stroke-dasharray="14 12" stroke-linecap="round"/>
    <path d="M520 -10 C 600 80, 700 120, 860 90" fill="none" stroke="var(--white)" stroke-width="5" stroke-dasharray="14 12" stroke-linecap="round"/>
    <g fill="var(--sparkle)">
      <path d="M110 40 l6 16 l16 6 l-16 6 l-6 16 l-6 -16 l-16 -6 l16 -6 Z"/>
      <path d="M720 160 l5 13 l13 5 l-13 5 l-5 13 l-5 -13 l-13 -5 l13 -5 Z"/>
      <path d="M250 95 l4 10 l10 4 l-10 4 l-4 10 l-4 -10 l-10 -4 l10 -4 Z"/>
      <path d="M790 300 l4 10 l10 4 l-10 4 l-4 10 l-4 -10 l-10 -4 l10 -4 Z"/>
    </g>
    <g fill="var(--sparkle-blue)">
      <path d="M380 30 l6 16 l16 6 l-16 6 l-6 16 l-6 -16 l-16 -6 l16 -6 Z"/>
      <path d="M640 45 l5 12 l12 5 l-12 5 l-5 12 l-5 -12 l-12 -5 l12 -5 Z"/>
    </g>
  </svg>

  <div class="brand">
    <span class="brand-dot"></span>
    <span class="brand-name">Bouncewell Events</span>
  </div>

  <div class="child child--boy" role="img" aria-label="Photo of a cheering young boy in a white shirt"></div>
  <div class="child child--girl" role="img" aria-label="Photo of an excited girl in a floral dress"></div>

  <div class="snapshot snapshot--left" role="img" aria-label="Photo of a red and black bouncy castle with slide on grass"></div>
  <div class="snapshot snapshot--centre" role="img" aria-label="Photo of a superhero themed inflatable bouncy castle"></div>
  <div class="snapshot snapshot--right" role="img" aria-label="Photo of a green jungle themed inflatable play area"></div>

  <h1 class="headline">The place<br>to have fun</h1>
  <p class="call-to-action">Book our bouncy castle and softplay!<br>Call +278 555 0142</p>
</main>
</body>
</html>
```